brisk-vale.com Real Estate, Investment, Financial corporate

Real Estate, Investment, Financial corporate looking site. Show present a professional firm, with an elegant display. Please see the attached file which includes the logo, palette and fonts.
Updates

We just starting the brief today. ( logo was delayed)

Target Market(s)

Investors, Corporate , B2b

Industry/Entity Type

real-estate investments

Number of Pages Required

3 page

Requirements
Must have
• Dazzling Homepage
Nice to have
• paralex

```html
<!DOCTYPE html>
<html lang="en">
<head>
<meta charset="utf-8">
<title>BRISK-VALE — Real Estate, Investment, Financial Corporate</title>
<link href="https://fonts.googleapis.com/css2?family=Roboto:wght@400;500;700&display=swap" rel="stylesheet">
<style>
:root{
  --blue:#1d44b0;
  --navy:#0f2f96;
  --panel:#4c6bcb;
  --ink:#111;
  --text:#333;
  --muted:#555;
  --line:#dcdcdc;
  --soft:#f4f4f4;
  --black:#0a0a0a;
  --white:#fff;
}
*{box-sizing:border-box;margin:0;padding:0}
html,body{width:1200px;height:4777px;overflow:hidden}
body{font-family:'Roboto',Arial,sans-serif;color:var(--text);background:var(--white);position:relative}
.btn{position:absolute;display:flex;align-items:center;justify-content:center;background:var(--navy);color:var(--white);border-radius:24px;font-size:16px;font-weight:500;letter-spacing:.3px}
.section-title{position:absolute;left:0;width:1200px;text-align:center;font-size:38px;font-weight:700;color:var(--ink)}
.lead{position:absolute;left:250px;width:700px;text-align:center;font-size:15.5px;line-height:29px;color:var(--ink);font-weight:500}

/* hero */
.hero{position:absolute;left:0;top:0;width:1200px;height:621px;background:linear-gradient(90deg,#e6e8ea 0%,#cfd6dc 30%,#7e8d9c 55%,#3b4553 80%,#2a2f38 100%)}
.hero-fade{position:absolute;left:0;top:0;width:1200px;height:621px;background:linear-gradient(90deg,rgba(255,255,255,.85) 0%,rgba(255,255,255,.6) 35%,rgba(255,255,255,0) 55%)}
.header-fade{position:absolute;left:0;top:0;width:1200px;height:110px;background:linear-gradient(180deg,rgba(255,255,255,.95),rgba(255,255,255,0))}
.logo{position:absolute;display:flex;align-items:center;gap:10px;font-size:27px;font-weight:500;color:var(--navy)}
.logo .dot{width:30px;height:30px;border-radius:50%;background:var(--navy)}
.nav{position:absolute;top:27px;font-size:16px;font-weight:500;color:var(--ink)}
.nav.active{color:var(--blue)}
.hero h1{position:absolute;left:111px;top:228px;font-size:62px;font-weight:700;color:var(--ink)}
.hero p{position:absolute;left:111px;top:305px;width:430px;font-size:17px;line-height:26px;font-weight:500;color:var(--ink)}
.arrow{position:absolute;top:312px}

/* services */
.svc{position:absolute;top:773px;width:313px;height:395px;border-radius:6px;overflow:hidden}
.svc .label{position:absolute;left:0;bottom:22px;width:100%;text-align:center;color:var(--white);font-size:21px;font-weight:500}
.svc.featured{background:var(--blue);color:var(--white);text-align:center}
.svc.featured h3{margin-top:88px;font-size:21px;font-weight:500}
.svc.featured p{margin:18px auto 0;width:270px;font-size:13px;line-height:27px}
.svc.featured a{display:inline-block;margin-top:14px;font-size:15px;font-weight:500;text-decoration:underline;color:var(--white)}

/* why */
.why{position:absolute;width:313px;height:300px;border:1px solid var(--line);background:var(--white);text-align:center}
.why::before{content:"";position:absolute;left:116px;top:-1px;width:80px;height:4px;background:var(--blue)}
.why svg{position:absolute;left:116px;top:30px}
.why h4{position:absolute;top:134px;left:0;width:100%;font-size:22px;font-weight:500;color:var(--ink)}
.why p{position:absolute;top:172px;left:14px;width:285px;font-size:13px;line-height:26px;color:var(--muted)}

/* video */
.video-band{position:absolute;left:0;top:2148px;width:1200px;height:468px;background:var(--blue)}
.video-frame{position:absolute;left:172px;top:2365px;width:854px;height:440px;border:4px solid var(--white);background:linear-gradient(135deg,#c9c2b6,#8a8d92 45%,#5c6470 70%,#2e3744);}
.play{position:absolute;left:387px;top:180px;width:80px;height:80px;border-radius:50%;background:var(--white);display:flex;align-items:center;justify-content:center}

/* about */
.about-ring{position:absolute;left:145px;top:2881px;width:408px;height:408px;border-radius:50%;border:4px solid var(--navy)}
.about-photo{position:absolute;left:153px;top:2875px;width:398px;height:398px;border-radius:50%;background:linear-gradient(135deg,#d6d9dd,#8d939b 50%,#4a4f58)}
.about-text{position:absolute;left:608px;top:2930px;width:450px}
.about-text .eyebrow{font-size:21px;font-weight:500;color:var(--blue)}
.about-text h2{font-size:38px;font-weight:500;color:var(--ink);margin-top:2px}
.about-text p{font-size:13px;line-height:26px;color:var(--muted);margin-top:14px}

/* news */
.news-bg{position:absolute;left:0;top:3376px;width:1200px;height:594px;background:var(--soft)}
.post{position:absolute;top:3512px;width:306px;height:378px;background:var(--white);border:1px solid var(--line)}
.post .thumb{position:absolute;left:12px;top:10px;width:282px;height:202px;border-radius:5px}
.post .meta{position:absolute;left:12px;top:232px;font-size:12.5px;color:var(--ink)}
.post .meta b{font-weight:400;color:var(--blue)}
.post h5{position:absolute;left:12px;top:256px;font-size:18px;font-weight:500;color:var(--ink)}
.post p{position:absolute;left:12px;top:286px;width:282px;font-size:13px;line-height:24px;color:var(--muted)}
.post a{position:absolute;left:12px;top:342px;font-size:13px;font-weight:700;color:var(--blue);text-decoration:none}

/* contact */
.contact-left{position:absolute;left:0;top:3970px;width:655px;height:482px;background:linear-gradient(135deg,#f1f2f3,#e3e6ea)}
.contact-right{position:absolute;left:655px;top:3970px;width:545px;height:482px;background:var(--panel)}
.form-title{position:absolute;left:111px;top:4040px;font-size:34px;font-weight:700;color:var(--ink)}
.underline{position:absolute;height:4px;width:66px;background:var(--navy)}
.field{position:absolute;background:var(--white);font-size:12.5px;color:var(--ink);padding:14px 12px}
.contact-right h2{position:absolute;left:122px;top:70px;font-size:34px;font-weight:700;color:var(--white);letter-spacing:1px}
.contact-right h6{position:absolute;left:122px;top:146px;font-size:16px;font-weight:700;color:var(--white)}
.ci{position:absolute;left:122px;display:flex;align-items:center;gap:14px;color:var(--white)}
.ci .ic{width:48px;height:48px;border-radius:50%;background:var(--white);display:flex;align-items:center;justify-content:center}
.ci .t{font-size:15px;line-height:19px}
.ci .t strong{font-size:18px;font-weight:700}

/* footer */
.footer{position:absolute;left:0;top:4452px;width:1200px;height:325px;background:var(--black);color:var(--white)}
.footer .logo{color:var(--white);left:475px;top:70px;font-size:32px}
.footer .logo .dot{background:var(--white)}
.fnav{position:absolute;top:143px;left:0;width:1200px;display:flex;justify-content:center;gap:32px;font-size:16px;font-weight:500}
.fnav span.sep{color:#aaa}
.copy{position:absolute;top:196px;left:0;width:1200px;text-align:center;font-size:14px;line-height:18px}
.social{position:absolute;top:234px;left:0;width:1200px;display:flex;justify-content:center;gap:10px}
.social span{width:42px;height:42px;border-radius:50%;background:var(--white)}
</style>
</head>
<body>

<!-- hero -->
<section class="hero">
  <div role="img" aria-label="Two business colleagues working at a laptop in a bright office overlooking a city" style="position:absolute;inset:0"></div>
  <div class="hero-fade"></div>
  <div class="header-fade"></div>
  <div class="logo" style="left:111px;top:20px"><span class="dot"></span>BRISK-VALE</div>
  <span class="nav active" style="left:466px">HOME</span>
  <span class="nav" style="left:554px">ABOUT</span>
  <span class="nav" style="left:646px">TEAM</span>
  <span class="nav" style="left:732px">SERVICES</span>
  <span class="nav" style="left:848px">NEWS</span>
  <div class="btn" style="left:928px;top:15px;width:160px;height:44px">CONTACT US</div>
  <h1>BRISK-VALE</h1>
  <p>Lorem ipsum dolor sit amet, consectetur adipiscing elit, sed do eiusmod tempor incididunt</p>
  <div class="btn" style="left:113px;top:380px;width:163px;height:45px">GET STARTED</div>
  <svg class="arrow" style="left:70px" width="20" height="36" viewBox="0 0 20 36"><path d="M17 2 3 18l14 16" fill="none" stroke="#333" stroke-width="2"/></svg>
  <svg class="arrow" style="left:1114px" width="20" height="36" viewBox="0 0 20 36"><path d="M3 2l14 16L3 34" fill="none" stroke="#fff" stroke-width="2"/></svg>
</section>

<!-- services -->
<h2 class="section-title" style="top:700px">OUR SERVICES</h2>
<div class="svc" style="left:111px;background:linear-gradient(160deg,#6b6258,#3a3530 55%,#1d1b1a)" role="img" aria-label="Hand passing house keys beside a small model house">
  <div class="label">REAL ESTATE</div>
</div>
<div class="svc featured" style="left:443px">
  <h3>INVESTMENT</h3>
  <p>Lorem ipsum dolor sit aonsectetur adipiscing elit, sed dempor incididunt ut labore et dolore magna aliqua. Quisum suspendisse ultrices gravida. Risus commodo viverra maecenas accumsan lacus vel facilisis.</p>
  <a>LEARN MORE »</a>
</div>
<div class="svc" style="left:775px;background:linear-gradient(160deg,#5a4a3c,#2e2722 55%,#151210)" role="img" aria-label="Smiling businessman in a meeting with a colleague">
  <div class="label">FINANCIAL CORPORATE</div>
</div>

<!-- why choose us -->
<h2 class="section-title" style="top:1275px">WHY CHOOSE US</h2>
<p class="lead" style="top:1326px">Lorem ipsum dolor sit amet, consectetur adipiscing elit, sed do eiusmod tempor incididunt ut labore et dolore magna aliqua. Quis ipsum suspendisse ultrices gravida.</p>

<div class="why" style="left:111px;top:1426px">
  <svg width="80" height="84" viewBox="0 0 80 84" fill="none" stroke="#1d44b0" stroke-width="2.5"><circle cx="40" cy="42" r="26"/><circle cx="40" cy="42" r="36" stroke-dasharray="10 6"/><path d="M32 34l16 16M48 34 32 50"/></svg>
  <h4>Finibus Bonorum ete</h4>
  <p>Lorem ipsum dolor sit amet, conetur adipiscing elit, sed do eiusmod tempor incidunt ut labore et dolore mna aliqua. Quis ipsum suspendisse ultrices gravida</p>
</div>
<div class="why" style="left:443px;top:1426px;box-shadow:0 6px 18px rgba(0,0,0,.08)">
  <svg width="80" height="84" viewBox="0 0 80 84" fill="none" stroke="#1d44b0" stroke-width="2.5"><rect x="8" y="18" width="40" height="56"/><path d="M8 18h40M16 28h6M30 28h6M16 40h6M30 40h6M16 52h6"/><circle cx="56" cy="62" r="16"/><path d="M56 52v20M61 56h-7a3 3 0 0 0 0 6h4a3 3 0 0 1 0 6h-7"/></svg>
  <h4>Finibus Bonorum ete</h4>
  <p>Lorem ipsum dolor sit amet, conetur adipiscing elit, sed do eiusmod tempor incidunt ut labore et dolore mna aliqua. Quis ipsum suspendisse ultrices gravida</p>
</div>
<div class="why" style="left:775px;top:1426px">
  <svg width="80" height="84" viewBox="0 0 80 84" fill="none" stroke="#1d44b0" stroke-width="2.5"><path d="M26 28 40 14l14 14v14H26z"/><rect x="36" y="32" width="8" height="10"/><path d="M10 44l14 22h10M70 44 56 66H46"/></svg>
  <h4>Finibus Bonorum ete</h4>
  <p>Lorem ipsum dolor sit amet, conetur adipiscing elit, sed do eiusmod tempor incidunt ut labore et dolore mna aliqua. Quis ipsum suspendisse ultrices gravida</p>
</div>
<div class="why" style="left:111px;top:1747px">
  <svg width="80" height="84" viewBox="0 0 80 84" fill="none" stroke="#1d44b0" stroke-width="2.5"><circle cx="24" cy="22" r="12"/><rect x="38" y="26" width="24" height="48"/><path d="M44 36h4M52 36h4M44 48h4M52 48h4M44 60h4M52 60h4M8 74h64M14 50v24M22 60v14"/></svg>
  <h4>Finibus Bonorum ete</h4>
  <p>Lorem ipsum dolor sit amet, conetur adipiscing elit, sed do eiusmod tempor incidunt ut labore et dolore mna aliqua. Quis ipsum suspendisse ultrices gravida</p>
</div>
<div class="why" style="left:443px;top:1747px">
  <svg width="80" height="84" viewBox="0 0 80 84" fill="none" stroke="#1d44b0" stroke-width="2.5"><circle cx="60" cy="20" r="12"/><path d="M60 8v12h12"/><rect x="46" y="46" width="8" height="22"/><rect x="58" y="38" width="8" height="30"/><path d="M10 70l14-20h12l-6 20zM24 44l6-8"/><circle cx="30" cy="38" r="8"/></svg>
  <h4>Finibus Bonorum ete</h4>
  <p>Lorem ipsum dolor sit amet, conetur adipiscing elit, sed do eiusmod tempor incidunt ut labore et dolore mna aliqua. Quis ipsum suspendisse ultrices gravida</p>
</div>
<div class="why" style="left:775px;top:1747px">
  <svg width="80" height="84" viewBox="0 0 80 84" fill="none" stroke="#1d44b0" stroke-width="2.5"><circle cx="40" cy="44" r="32"/><path d="M28 40 40 28l12 12v16H28z"/><circle cx="18" cy="44" r="7"/><circle cx="62" cy="44" r="7"/><circle cx="40" cy="16" r="6"/></svg>
  <h4>Finibus Bonorum ete</h4>
  <p>Lorem ipsum dolor sit amet, conetur adipiscing elit, sed do eiusmod tempor incidunt ut labore et dolore mna aliqua. Quis ipsum suspendisse ultrices gravida</p>
</div>

<!-- company video -->
<section class="video-band">
  <h2 class="section-title" style="top:68px;color:var(--white)">OUR COMPANY VIDEO</h2>
  <p class="lead" style="top:118px;color:var(--white)">Lorem ipsum dolor sit amet, consectetur adipiscing elit, sed do eiusmod tempor incididunt ut labore et dolore magna aliqua. Quis ipsum suspendisse ultrices gravida.</p>
</section>
<div class="video-frame" role="img" aria-label="Three colleagues reviewing plans together at a table">
  <div class="play"><svg width="24" height="26" viewBox="0 0 24 26"><path d="M4 2l18 11L4 24z" fill="#1d44b0"/></svg></div>
</div>

<!-- who we are -->
<div class="about-ring"></div>
<div class="about-photo" role="img" aria-label="Three business people discussing over a tablet"></div>
<div class="about-text">
  <div class="eyebrow">Who We Are</div>
  <h2>BRISK-VALE</h2>
  <p>Lorem ipsum dolor sit amet, consectetu sed do eiusmod tempor incididunt ut labore et dolore na alium suspendisse ultrices gravida. Risus commodo viverra maecenas us vel facilisis. Lorem ipsum dolor sit amet, consectetur adipiscing elit, sed do</p>
  <p>Lorem ipsum dolor sit amet, consectetu sed do eiusmod tempor incididunt ut labore et dolore na alium suspendisse ultrices gravida.</p>
</div>
<div class="btn" style="left:609px;top:3198px;width:163px;height:42px">LEARN MORE</div>

<!-- news -->
<div class="news-bg"></div>
<h2 class="section-title" style="top:3446px">OUR NEWS AND BLOG</h2>
<article class="post" style="left:111px">
  <div class="thumb" role="img" aria-label="Model city buildings on a desk" style="background:linear-gradient(135deg,#e8eaec,#9aa0a6 55%,#3f454c)"></div>
  <div class="meta">By <b>brisk-vale</b> &nbsp;|&nbsp; 18 Aug 2021</div>
  <h5>The sandard Lorem Ipsum pass</h5>
  <p>Lorem ipsum dolor sit amet, conse adipiscing elit, sed do eiusmod tempor</p>
  <a>LEARN MORE &gt;&gt;</a>
</article>
<article class="post" style="left:445px;box-shadow:0 6px 18px rgba(0,0,0,.08)">
  <div class="thumb" role="img" aria-label="Financial charts, glasses and a calculator on a desk" style="background:linear-gradient(135deg,#c7cbd0,#6e747c 55%,#2a2e34)"></div>
  <div class="meta">By <b>brisk-vale</b> &nbsp;|&nbsp; 18 Aug 2021</div>
  <h5>The sandard Lorem Ipsum pass</h5>
  <p>Lorem ipsum dolor sit amet, conse adipiscing elit, sed do eiusmod tempor</p>
  <a>LEARN MORE &gt;&gt;</a>
</article>
<article class="post" style="left:779px">
  <div class="thumb" role="img" aria-label="Hand stacking coins in rising columns" style="background:linear-gradient(135deg,#f0e4e2,#b79a93 55%,#4a3a36)"></div>
  <div class="meta">By <b>brisk-vale</b> &nbsp;|&nbsp; 18 Aug 2021</div>
  <h5>The sandard Lorem Ipsum pass</h5>
  <p>Lorem ipsum dolor sit amet, conse adipiscing elit, sed do eiusmod tempor</p>
  <a>LEARN MORE &gt;&gt;</a>
</article>

<!-- contact -->
<div class="contact-left" role="img" aria-label="Faded office desk with charts in the background"></div>
<h2 class="form-title">GET IN TOUCH</h2>
<div class="underline" style="left:111px;top:4087px"></div>
<div class="field" style="left:111px;top:4113px;width:238px;height:46px">Your Name</div>
<div class="field" style="left:358px;top:4113px;width:238px;height:46px">Phone</div>
<div class="field" style="left:111px;top:4168px;width:238px;height:46px">Email address</div>
<div class="field" style="left:358px;top:4168px;width:238px;height:46px">Subject</div>
<div class="field" style="left:111px;top:4224px;width:485px;height:87px">Message</div>
<div class="btn" style="left:111px;top:4328px;width:162px;height:44px">SUBMIT</div>

<section class="contact-right">
  <h2>CONTACT &nbsp;US</h2>
  <h6>OUR VISIT US</h6>
  <div class="ci" style="top:180px">
    <span class="ic"><svg width="20" height="24" viewBox="0 0 20 24"><path d="M10 1a8 8 0 0 0-8 8c0 6 8 14 8 14s8-8 8-14a8 8 0 0 0-8-8z" fill="#1d44b0"/><circle cx="10" cy="9" r="3" fill="#fff"/></svg></span>
    <span class="t">1234 Somestreet Anywhere<br>USA 21212</span>
  </div>
  <div class="ci" style="top:249px">
    <span class="ic"><svg width="20" height="20" viewBox="0 0 20 20"><path d="M4 1l4 4-2 3c1 2 3 4 5 5l3-2 4 4-3 3C8 18 2 12 1 4z" fill="#1d44b0"/></svg></span>
    <span class="t">Call Us Today!<br><strong>123 456 7890</strong></span>
  </div>
  <div class="ci" style="top:316px">
    <span class="ic"><svg width="22" height="16" viewBox="0 0 22 16"><rect x="1" y="1" width="20" height="14" fill="#1d44b0"/><path d="M1 1l10 8 10-8" fill="none" stroke="#fff" stroke-width="1.5"/></svg></span>
    <span class="t">Email Us<br><strong>info@briskvale.com</strong></span>
  </div>
</section>

<!-- footer -->
<footer class="footer">
  <div class="logo"><span class="dot"></span>BRISK-VALE</div>
  <nav class="fnav">
    <span>HOME</span><span class="sep">|</span><span>ABOUT</span><span class="sep">|</span><span>TEAM</span><span class="sep">|</span><span>SERVICES</span><span class="sep">|</span><span>NEWS</span><span class="sep">|</span><span>CONTACT US</span>
  </nav>
  <div class="copy">©Copyright ©2021brisk-vale . All Rights Reserved.</div>
  <div class="social" aria-label="Social links">
    <span></span><span></span><span></span><span></span>
  </div>
</footer>

</body>
</html>
```